Bold Flyer Needed for Bold Little Gym

We need a 1 page flyer created for our small boutique fitness facility, KorVesta, which highlights a new service we are offering.
We are now offering Red Light Therapy (RLT) to our members and I need a full color, 1 page flyer created that captures the eye of our members while highlighting the benefits and clearly stating the prices at the bottom of the page.
Flyer will be printed out on a standard 8.5" x 11" sheet of paper and should be laid out in a way that is easy to read. Landscape or Portrait layouts are both expectable.
We are using Quorvane Glow Therapy Lights TelaRix 700 Lamps as found here http://lnkzo.example/7QWPL4M
I have attached the text that should be included and our logo for branding of the flyer.
Thank you!

```html
<!DOCTYPE html>
<html lang="en">
<head>
<meta charset="UTF-8">
<title>KorVesta Red Light Therapy Flyer</title>
<link href="https://fonts.googleapis.com/css2?family=Exo+2:ital,wght@0,700;0,800;1,800;1,900&family=Open+Sans:wght@400;600;700;800&display=swap" rel="stylesheet">
<style>
  :root {
    --stage: #343a48;
    --ink: #050505;
    --gold: #ffcc00;
    --gold-deep: #e0ad00;
    --amber: #b88400;
    --bronze: #6b3f00;
    --paper-text: #ffffff;
    --muted: #cfcfcf;
  }
  * { box-sizing: border-box; margin: 0; padding: 0; }
  html, body { width: 1200px; height: 900px; overflow: hidden; }
  body {
    background: var(--stage);
    font-family: "Open Sans", sans-serif;
    position: relative;
  }
  .flyer {
    position: absolute;
    top: 140px;
    width: 480px;
    height: 621px;
    background: var(--ink);
    overflow: hidden;
    color: var(--paper-text);
  }
  .flyer--back { left: 90px; }
  .flyer--front { left: 630px; }
  .abs { position: absolute; }

  .brand {
    display: flex; align-items: center; gap: 6px;
    font-family: "Open Sans", sans-serif;
    font-weight: 800; font-size: 24px; color: var(--gold);
    letter-spacing: -0.5px;
  }
  .brand__mark { width: 12px; height: 12px; background: var(--gold); }

  .chevrons { width: 70px; height: 20px; }
  .photo { border-radius: 2px; }

  /* back */
  .intro {
    left: 110px; top: 82px; width: 300px;
    font-size: 10px; line-height: 1.35; text-align: center;
  }
  .info-column {
    left: 205px; top: 160px; width: 255px;
    display: flex; flex-direction: column; gap: 10px;
  }
  .section-title {
    font-weight: 700; color: var(--gold); font-size: 15px; line-height: 1.2;
  }
  .benefits__list { list-style: none; margin-top: 8px; }
  .benefits__list li { font-weight: 700; font-size: 12px; line-height: 1.55; }
  .why__item { font-size: 8.5px; line-height: 1.35; color: var(--muted); margin-top: 5px; }
  .offer {
    left: 130px; top: 448px; width: 320px; text-align: center;
    font-size: 11px; line-height: 1.4;
  }
  .offer__lead { font-weight: 700; }
  .offer__price { color: var(--gold); }
  .offer__small { font-size: 9.5px; color: var(--muted); }
  .tagline {
    left: 210px; top: 562px; width: 240px;
    color: var(--gold); font-weight: 800; font-size: 14px; line-height: 1.3;
  }

  /* front */
  .headline {
    right: 28px; top: 112px;
    font-family: "Exo 2", sans-serif; font-style: italic; font-weight: 900;
    font-size: 54px; line-height: 0.95; color: var(--gold); text-align: right;
    text-transform: uppercase;
  }
  .prices {
    left: 232px; top: 338px; width: 224px; height: 150px;
    background: var(--gold); color: var(--ink); border-radius: 28px;
    padding: 14px 14px;
    font-family: "Exo 2", sans-serif; font-style: italic; font-weight: 800;
  }
  .prices table { width: 100%; border-collapse: collapse; }
  .prices th { font-size: 10px; text-align: left; padding-bottom: 6px; text-transform: uppercase; }
  .prices td { font-size: 10px; padding: 3px 0; text-transform: uppercase; }
  .prices td.num, .prices th.num { text-align: center; }
  .contact-pill {
    left: 22px; top: 440px; width: 210px; height: 70px;
    background: var(--ink); border-radius: 24px;
    color: var(--gold); text-align: center; padding-top: 12px;
  }
  .contact-pill__phone { font-family: "Exo 2", sans-serif; font-weight: 700; font-size: 20px; }
  .contact-pill__web { font-size: 12px; margin-top: 2px; }
  .visit {
    left: 244px; top: 500px; width: 210px;
    font-size: 11px; line-height: 1.4; text-align: center; font-weight: 600;
  }
  .visit__phone { color: var(--gold); white-space: nowrap; }
  .join {
    left: 236px; top: 566px; width: 210px; height: 32px;
    background: var(--gold); color: var(--ink);
    font-family: "Exo 2", sans-serif; font-style: italic; font-weight: 900;
    font-size: 17px; text-align: center; line-height: 32px; text-transform: uppercase;
  }
</style>
</head>
<body>

<section class="flyer flyer--back">
  <svg class="abs chevrons" style="left:390px;top:22px" viewBox="0 0 70 20">
    <g fill="var(--gold)"><path d="M0 2h6l8 8-8 8H0l8-8z"/><path d="M16 2h6l8 8-8 8h-6l8-8z"/><path d="M32 2h6l8 8-8 8h-6l8-8z"/><path d="M48 2h6l8 8-8 8h-6l8-8z"/></g>
  </svg>

  <div class="abs brand" style="left:175px;top:40px"><span class="brand__mark"></span>KorVesta</div>

  <p class="abs intro">Unlock Your Potential with Red Light Therapy at KorVesta! Introducing Our New Red Light Therapy Room! Transform Your Wellness Routine with the Power of Light! What is Red Light Therapy?</p>

  <div class="abs photo" role="img" aria-label="Gym equipment close-up" style="left:438px;top:88px;width:42px;height:60px;background:linear-gradient(160deg,#5a4a3e,#2a221c)"></div>

  <svg class="abs" style="left:0;top:148px" width="120" height="80" viewBox="0 0 120 80">
    <polygon points="0,22 40,0 80,14 40,36" fill="var(--gold)"/>
    <polygon points="0,28 50,48 110,52 60,32" fill="var(--gold-deep)"/>
    <polygon points="30,56 90,78 120,78 70,56" fill="var(--gold)"/>
  </svg>

  <div class="abs photo" role="img" aria-label="Woman training with battle ropes in a gym" style="left:28px;top:232px;width:160px;height:200px;background:linear-gradient(170deg,#6b6256,#3a2f28 55%,#c85a20)"></div>

  <div class="abs info-column">
    <div class="benefits">
      <h2 class="section-title">Benefits of Quorvane Glow Therapy:</h2>
      <ul class="benefits__list">
        <li>Boosts Energy Levels</li>
        <li>Enhances Muscle Recovery</li>
        <li>Improves Skin Health</li>
        <li>Supports Joint Health</li>
        <li>Promotes Better Sleep</li>
        <li>Increases Circulation</li>
      </ul>
    </div>
    <div class="why">
      <h2 class="section-title">Why Choose KorVesta?</h2>
      <p class="why__item">State-of-the-Art Equipment: Experience the power of TelaRix 700 panels—some of the best on the market.</p>
      <p class="why__item">Expert Guidance: Our trained staff will guide you to ensure you get the most out of your session.</p>
      <p class="why__item">Community Focused: Join a supportive community that prioritizes your wellness.</p>
    </div>
  </div>

  <div class="abs offer">
    <p class="offer__lead">Special Introductory Offer!</p>
    <p>Try Your First Session for <span class="offer__price">Just $25!</span></p>
    <p class="offer__lead">(Regularly $55)</p>
    <p class="offer__small">Limited Time Only!</p>
    <p class="offer__small">Book your session today and discover how Red Light Therapy can elevate your fitness journey.</p>
    <p class="offer__small">Ready to Shine?</p>
  </div>

  <div class="abs photo" role="img" aria-label="Woman lifting dumbbells in a gym" style="left:40px;top:556px;width:150px;height:58px;background:linear-gradient(160deg,#4a3a40,#2a1e22 50%,#8a2a2a)"></div>

  <p class="abs tagline">KorVesta Fitness Facility, Your Wellness, Our Commitment!</p>

  <svg class="abs" style="right:0;top:500px" width="30" height="60" viewBox="0 0 30 60">
    <polygon points="0,0 18,4 16,50 0,46" fill="var(--bronze)"/>
    <polygon points="18,4 30,10 30,60 16,50" fill="var(--amber)"/>
  </svg>
</section>

<section class="flyer flyer--front">
  <div class="abs brand" style="left:30px;top:28px"><span class="brand__mark"></span>KorVesta</div>

  <svg class="abs chevrons" style="left:30px;top:72px" viewBox="0 0 70 20">
    <g fill="var(--gold)"><path d="M0 2h6l8 8-8 8H0l8-8z"/><path d="M16 2h6l8 8-8 8h-6l8-8z"/><path d="M32 2h6l8 8-8 8h-6l8-8z"/><path d="M48 2h6l8 8-8 8h-6l8-8z"/></g>
  </svg>
  <svg class="abs chevrons" style="left:290px;top:88px" viewBox="0 0 70 20">
    <g fill="var(--gold)"><path d="M0 2h6l8 8-8 8H0l8-8z"/><path d="M16 2h6l8 8-8 8h-6l8-8z"/><path d="M32 2h6l8 8-8 8h-6l8-8z"/><path d="M48 2h6l8 8-8 8h-6l8-8z"/></g>
  </svg>

  <svg class="abs" style="right:0;top:60px" width="90" height="110" viewBox="0 0 90 110">
    <polygon points="0,0 40,0 90,40 90,110" fill="var(--gold)"/>
    <polygon points="40,0 90,0 90,40" fill="var(--gold-deep)"/>
    <polygon points="50,30 70,40 75,100 60,85" fill="var(--ink)"/>
  </svg>

  <div class="abs photo" role="img" aria-label="Athletic woman training with a dumbbell in a dark gym" style="left:18px;top:118px;width:240px;height:300px;background:linear-gradient(160deg,#3a2c22,#8a6040 45%,#1a1410)"></div>

  <svg class="abs" style="left:0;top:320px" width="300" height="301" viewBox="0 0 300 301">
    <polygon points="0,60 140,0 300,200 300,301 0,301" fill="var(--amber)"/>
    <polygon points="0,150 180,100 300,301 0,301" fill="var(--gold-deep)"/>
    <polygon points="0,60 60,40 0,170" fill="var(--gold)"/>
  </svg>

  <h1 class="abs headline">Lets<br>Push<br>The<br>Limit</h1>

  <div class="abs prices">
    <table>
      <thead>
        <tr><th>Prices</th><th class="num">KorVesta Member</th><th class="num">Non-Member</th></tr>
      </thead>
      <tbody>
        <tr><td>Single Session</td><td class="num">$35</td><td class="num">$55</td></tr>
        <tr><td>3 - Pack</td><td class="num">$102</td><td class="num">$159</td></tr>
        <tr><td>5 - Pack</td><td class="num">$167</td><td class="num">$259</td></tr>
        <tr><td>10 - Pack</td><td class="num">$316</td><td class="num">$491</td></tr>
      </tbody>
    </table>
  </div>

  <div class="abs contact-pill">
    <p class="contact-pill__phone">123-456-7890</p>
    <p class="contact-pill__web">www.korvesta-studio.example</p>
  </div>

  <p class="abs visit">Visit our front desk or call us at <span class="visit__phone">(555) 014-2298</span> to schedule your appointment.</p>

  <div class="abs join">Join Now</div>
</section>

</body>
</html>
```